Website To Serve As A Resource For Medical Conditions

I need a website that is attractive that will be utilized to educate patients on either hepatitis c or HIV so it should be easily readable attractive but also professional. This website is going to be furnished with various topics for example, HIV treatment, HIV and Nutrition, HIV and Exercise, HIV and....

This website will also be cloned and utilized similarly for Hepatitis.

Coded - Design and coding required

1 page

0094D4
00A9DD
6FCCEA
C7EBF8
E9F6FB
A7469A
B969AE
D3A5CF
EDDBEB
F8F0F9
6B429C
8869AF
B7A5CE
E3DAEB
F3F0F8

```html
<!DOCTYPE html>
<html lang="en">
<head>
<meta charset="utf-8">
<title>HIV Conditions</title>
<link rel="stylesheet" href="https://fonts.googleapis.com/css2?family=Roboto+Condensed:wght@700&family=Roboto:wght@400;500;700&display=swap">
<style>
:root{
  --blue:#0094D4;
  --blue-bright:#00A9DD;
  --blue-soft:#6FCCEA;
  --blue-pale:#C7EBF8;
  --blue-mist:#E9F6FB;
  --ink:#111111;
  --text:#555555;
  --white:#ffffff;
  --black:#000000;
}
*{margin:0;padding:0;box-sizing:border-box}
html,body{width:1200px;height:4191px;overflow:hidden}
body{position:relative;background:var(--white);font-family:'Roboto',Arial,sans-serif;color:var(--text)}
.abs{position:absolute}
.heading{font-family:'Roboto Condensed','Arial Narrow',sans-serif;font-weight:700;color:var(--ink);text-transform:uppercase;line-height:1}
.rule{position:absolute;height:4px;background:var(--blue)}
.btn{position:absolute;display:flex;align-items:center;justify-content:center;background:var(--blue);color:var(--white);font-weight:700;font-size:15px;border-radius:3px;text-decoration:none}

.top-line{top:0;left:0;width:1200px;height:3px;background:var(--blue)}
.brand{left:107px;top:78px;display:flex;align-items:center;gap:12px}
.brand-mark{width:18px;height:18px;border-radius:50%;background:var(--blue)}
.brand-name{font-family:'Roboto',sans-serif;font-weight:500;font-size:26px;color:var(--blue);line-height:1}
.nav{top:117px;left:462px;width:632px;display:flex;justify-content:space-between;font-size:13px;color:#666}

.hero-art{left:712px;top:252px;width:488px;height:488px;border-radius:50%;background:radial-gradient(circle at 40% 35%,var(--blue-pale),var(--blue-bright) 55%,var(--blue) 100%)}
.hero-wash{left:0;top:480px;width:1200px;height:260px;background:linear-gradient(90deg,rgba(255,255,255,0),var(--blue-mist))}
.hero-title-1{left:109px;top:316px;font-size:56px}
.hero-title-2{left:107px;top:380px;font-size:72px;color:var(--blue)}
.hero-copy{left:109px;top:474px;width:550px;font-size:16px;line-height:32px}

.center{left:0;width:1200px;text-align:center}
.section-copy{font-size:14px;line-height:28px}

.card{position:absolute;top:1046px;width:314px;height:391px;border-radius:28px;background:var(--white);box-shadow:0 4px 14px rgba(0,0,0,.08);text-align:center}
.card.active{background:var(--blue);color:var(--white);border-radius:0 36px 0 36px;box-shadow:none}
.card-icon{width:84px;height:84px;border-radius:50%;background:var(--blue);margin:47px auto 0;display:flex;align-items:center;justify-content:center}
.card.active .card-icon{background:var(--white)}
.card-title{font-family:'Roboto Condensed',sans-serif;font-weight:700;font-size:16px;color:var(--ink);margin-top:28px}
.card.active .card-title{color:var(--white)}
.card-text{font-size:12.5px;line-height:24px;margin:12px 34px 0}

.nutrition-art{left:0;top:1545px;width:472px;height:585px;background:linear-gradient(160deg,var(--white),#f1f1f1)}
.exercise{left:0;top:2133px;width:1200px;height:687px;background:linear-gradient(90deg,var(--blue) 0%,var(--blue-bright) 100%)}
.exercise-art{left:605px;top:2215px;width:483px;height:523px;background:linear-gradient(160deg,#ffffff,#e9ecef)}
.people-art{left:0;top:3358px;width:1200px;height:569px;background:linear-gradient(180deg,#ffffff 0%,#ededed 60%,#d9d9d9 100%)}

.footer{left:0;top:3927px;width:1200px;height:264px;background:var(--black)}
.footer-brand{left:110px;top:4040px;display:flex;align-items:center;gap:14px}
.footer-brand .brand-mark{background:var(--white);width:22px;height:22px}
.footer-brand .brand-name{color:var(--white);font-size:32px}
.footer-nav{top:4008px;left:561px;width:528px;display:flex;justify-content:space-between;font-size:13px;color:var(--white)}
.social{top:4052px;left:981px;display:flex;gap:6px}
.social span{width:32px;height:32px;border-radius:50%;background:var(--white);display:block;border:4px solid var(--blue)}
.copyright{top:4108px;right:111px;font-size:11px;color:var(--white)}
</style>
</head>
<body>
<div class="abs top-line"></div>

<header>
  <div class="abs brand"><span class="brand-mark"></span><span class="brand-name">Positive Path</span></div>
  <a class="btn" style="left:810px;top:55px;width:131px;height:43px">Get Started</a>
  <a class="btn" style="left:959px;top:55px;width:134px;height:43px">Get A Quote</a>
  <nav class="abs nav"><span>Home</span><span>HIV treatment</span><span>HIV &amp; Nutrition</span><span>HIV &amp; Exercise</span><span>HIV &amp; others</span><span>Contact Us</span></nav>
</header>

<section class="hero">
  <div class="abs hero-wash"></div>
  <div class="abs hero-art" role="img" aria-label="Globe with a red awareness ribbon"></div>
  <h1 class="abs heading hero-title-1">Welcome to</h1>
  <h1 class="abs heading hero-title-2">HIV Conditions</h1>
  <p class="abs hero-copy">On the other hand, we denounce with righteous indignation and dislike men who are so beguiled and demoralized by the charms of pleasure of the moment, so blinded by desire, that they</p>
  <a class="btn" style="left:109px;top:595px;width:132px;height:43px">Get Started</a>
</section>

<section class="treatment">
  <h2 class="abs heading center" style="top:838px;font-size:50px">HIV Treatment</h2>
  <div class="rule" style="left:535px;top:910px;width:128px"></div>
  <p class="abs center section-copy" style="top:941px;padding:0 179px">On the other hand, we denounce with righteous indignation and dislike men who are so beguiled and demoralized by the charms of pleasure of the moment, so blinded by desire, that they cannot foresee the pain and trouble that are bound to ensue</p>

  <div class="card" style="left:94px">
    <div class="card-icon"><svg width="44" height="44" viewBox="0 0 44 44" fill="none" stroke="#fff" stroke-width="3"><circle cx="22" cy="22" r="12"/><path d="M22 4v6M22 34v6M4 22h6M34 22h6M9 9l4 4M31 31l4 4M35 9l-4 4M13 31l-4 4"/></svg></div>
    <h3 class="card-title">Eos et accusamus et iusto odio</h3>
    <p class="card-text">On the other hand, we denounce with righteous indignation and dislike men who are so beguiled and demoralized by the charms of pleasure of the moment, so blinded by desire, that they cannot foresee the pain and trouble that are bound to ensue; and equal blame</p>
  </div>
  <div class="card active" style="left:444px">
    <div class="card-icon"><svg width="44" height="44" viewBox="0 0 44 44" fill="none" stroke="#0094D4" stroke-width="3"><path d="M22 38s-14-9-14-19a8 8 0 0 1 14-5 8 8 0 0 1 14 5c0 10-14 19-14 19z"/></svg></div>
    <h3 class="card-title">Eos et accusamus et iusto odio</h3>
    <p class="card-text">On the other hand, we denounce with righteous indignation and dislike men who are so beguiled and demoralized by the charms of pleasure of the moment, so blinded by desire, that they cannot foresee the pain and trouble that are bound to ensue; and equal blame</p>
  </div>
  <div class="card" style="left:792px">
    <div class="card-icon"><svg width="44" height="44" viewBox="0 0 44 44" fill="none" stroke="#fff" stroke-width="3"><circle cx="22" cy="12" r="6"/><rect x="6" y="24" width="32" height="12" rx="4"/><path d="M12 30h12"/></svg></div>
    <h3 class="card-title">Eos et accusamus et iusto odio</h3>
    <p class="card-text">On the other hand, we denounce with righteous indignation and dislike men who are so beguiled and demoralized by the charms of pleasure of the moment, so blinded by desire, that they cannot foresee the pain and trouble that are bound to ensue; and equal blame</p>
  </div>
</section>

<section class="nutrition">
  <div class="abs nutrition-art" role="img" aria-label="Line drawing of a hand reaching toward a red awareness ribbon"></div>
  <h2 class="abs heading" style="right:112px;top:1595px;font-size:50px">HIV and Nutrition</h2>
  <div class="rule" style="left:958px;top:1666px;width:128px"></div>
  <p class="abs section-copy" style="left:578px;top:1698px;width:510px;text-align:right;line-height:28.4px">On the other hand, we denounce with righteous indignation and dislike men who are so beguiled and demoralized by the charms of pleasure of the moment, so blinded by desire, that they cannot foresee the pain and trouble that are bound to ensue; and equal blame belongs to those who fail in their duty through weakness of will, which is the same as saying through shrinking from toil and pain. These cases are perfectly simple and easy to distinguish. In a free hour, when our power of choice is untrammelled and when nothing prevents our being able to do what we like best, every pleasure is to be welcomed and every pain avoided. But in certain circumstances and owing to the claims of duty or the obligations of business</p>
  <a class="btn" style="left:971px;top:2010px;width:115px;height:42px">Read More</a>
</section>

<section>
  <div class="abs exercise" role="img" aria-label="Blue band over a faint photo of a person exercising"></div>
  <h2 class="abs heading" style="left:109px;top:2258px;font-size:50px;color:var(--white)">HIV and Exercise</h2>
  <div class="rule" style="left:109px;top:2331px;width:128px;background:var(--white)"></div>
  <p class="abs section-copy" style="left:111px;top:2361px;width:436px;color:var(--white);line-height:28.4px">On the other hand, we denounce with righteous indignation and dislike men who are so beguiled and demoralized by the charms of pleasure of the moment, so blinded by desire, that they cannot foresee the pain and trouble that are bound to ensue; and equal blame belongs to those who fail in their duty through weakness of will, which is the same as saying through shrinking from toil and pain. These cases are perfectly simple and easy to distinguish. In a free hour, when our power of choice is untrammelled and when nothing prevents our being able</p>
  <a class="btn" style="left:111px;top:2647px;width:116px;height:43px;background:var(--white);color:var(--blue)">Read More</a>
  <div class="abs exercise-art" role="img" aria-label="Aerial view of a crowd forming an awareness ribbon shape"></div>
</section>

<section>
  <h2 class="abs heading center" style="top:2928px;font-size:50px">HIV and Others</h2>
  <div class="rule" style="left:536px;top:3000px;width:128px"></div>
  <p class="abs center" style="top:3035px;padding:0 165px;font-size:16px;line-height:31.5px">On the other hand, we denounce with righteous indignation and dislike men who are so beguiled and demoralized by the charms of pleasure of the moment, so blinded by desire, that they cannot foresee the pain and trouble that are bound to ensue; and equal blame belongs to those who fail in their duty through weakness of will, which is the same as saying through shrinking from toil and pain. These cases are perfectly simple and easy to distinguish.</p>
  <p class="abs center" style="top:3192px;padding:0 150px;font-size:16px;line-height:31.5px">In a free hour, when our power of choice is untrammelled and when nothing prevents our being able to do what we like best, every pleasure is to be welcomed and every pain avoided. But in certain circumstances and owing to the claims of duty or the obligations of business it will frequently occur that pleasures have to be repudiated and annoyances</p>
  <a class="btn" style="left:537px;top:3314px;width:125px;height:42px">Join With Us</a>
  <div class="abs people-art" role="img" aria-label="Group of five people in white shirts wearing red awareness ribbons"></div>
</section>

<footer>
  <div class="abs footer"></div>
  <div class="abs footer-brand"><span class="brand-mark"></span><span class="brand-name">Positive Path</span></div>
  <nav class="abs footer-nav"><span>Home</span><span>HIV treatment</span><span>HIV &amp; Nutrition</span><span>HIV &amp; Exercise</span><span>HIV &amp; others</span></nav>
  <div class="abs social"><span></span><span></span><span></span></div>
  <p class="abs copyright">© Copyrights 2023 | All Rights Reserved</p>
</footer>
</body>
</html>
```